Paper Lantern Theory - Podcast Cover

Paper Lantern Theory is a weekly podcast that dispels some of the myths about conventional economic thinking and provides a new way of thinking about issues that are faced by the global economy. It's insightful, thought-provoking and, most importantly, fun. We are refreshing the look and sound of the podcast. I have attached a copy of the old amateur design (which I did!)

Target Market(s)

Male oriented, smart folk with an interest in politics and economics

Font styles to use
Sans Serif

Requirements
Must have
• Clearly visible title, even when reduced in size. Must be 3000 pixels by 3000 pixels.
Nice to have
• This podcast challenges the status quo. It should reflect that. Photos and names of the hosts. Actually, because th ephotos are so different, we'd be open to the idea of a caricature if you can do that within the price.

```html
<!DOCTYPE html>
<html lang="en">
<head>
<meta charset="utf-8">
<title>Paper Lantern Theory Podcast Cover</title>
<link rel="stylesheet" href="https://fonts.googleapis.com/css2?family=Bebas+Neue&family=Roboto+Condensed:wght@500&display=swap">
<style>
  :root {
    --orange: #ea5a22;
    --band-orange: #ec5a20;
    --blue: #1f7bd0;
    --white: #ffffff;
    --strip-top: #dff0f6;
    --strip-bottom: #f4f0f2;
    --yellow: #f5b400;
    --purple: #8250a0;
    --raspberry: #e3245a;
    --cream: #f3e6cf;
    --teal: #2a8a7c;
  }
  * { margin: 0; padding: 0; box-sizing: border-box; }
  html, body {
    width: 1200px;
    height: 1200px;
    overflow: hidden;
    background: var(--orange);
  }
  .cover {
    position: relative;
    width: 1200px;
    height: 1200px;
    overflow: hidden;
    background: var(--orange);
  }
  .artwork {
    position: absolute;
    inset: 0;
  }
  .title-band {
    position: absolute;
    left: 0;
    top: 828px;
    width: 1200px;
    height: 296px;
    background: var(--band-orange);
  }
  .bottom-strip {
    position: absolute;
    left: 0;
    top: 1124px;
    width: 1200px;
    height: 76px;
    background: linear-gradient(90deg, var(--strip-top), var(--strip-bottom) 55%, #eaf3f7);
  }
  .title {
    position: absolute;
    left: 360px;
    top: 774px;
    width: 480px;
    color: var(--white);
    font-family: "Bebas Neue", "Oswald", sans-serif;
    line-height: 1;
  }
  .title-kicker {
    display: block;
    font-size: 92px;
    line-height: 82px;
    letter-spacing: 0;
  }
  .title-main {
    display: block;
    font-size: 156px;
    line-height: 118px;
    letter-spacing: 1px;
  }
  .title-format {
    display: block;
    margin-top: 2px;
    text-align: right;
    padding-right: 4px;
    font-family: "Roboto Condensed", "Arial Narrow", sans-serif;
    font-weight: 500;
    font-size: 40px;
    line-height: 40px;
  }
</style>
</head>
<body>
<main class="cover">
  <svg class="artwork" width="1200" height="1200" viewBox="0 0 1200 1200" xmlns="http://www.w3.org/2000/svg">
    <defs>
      <linearGradient id="host-left-tone" x1="0" y1="0" x2="0" y2="1">
        <stop offset="0" stop-color="#e7b8a6"/>
        <stop offset="0.55" stop-color="#d9917f"/>
        <stop offset="1" stop-color="#3f8fd1"/>
      </linearGradient>
      <linearGradient id="host-right-tone" x1="0" y1="0" x2="0" y2="1">
        <stop offset="0" stop-color="#c9a590"/>
        <stop offset="0.55" stop-color="#d79a7e"/>
        <stop offset="1" stop-color="#f1e6e2"/>
      </linearGradient>
    </defs>

    <circle class="backdrop-disc" cx="598" cy="602" r="458" fill="var(--blue)"/>

    <circle class="orbit-dots" cx="598" cy="600" r="595" fill="none" stroke="var(--white)" stroke-width="5" stroke-linecap="round" stroke-dasharray="0 17"/>
    <circle class="orbit-line" cx="598" cy="600" r="532" fill="none" stroke="var(--white)" stroke-width="4"/>

    <g class="topic-icons">
      <circle cx="66" cy="618" r="58" fill="var(--yellow)" role="img" aria-label="Calculator icon"/>
      <circle cx="102" cy="406" r="58" fill="var(--purple)" role="img" aria-label="Dog icon"/>
      <circle cx="216" cy="224" r="58" fill="var(--raspberry)" role="img" aria-label="Syringe icon"/>
      <circle cx="396" cy="104" r="58" fill="var(--yellow)" role="img" aria-label="Graduation cap icon"/>
      <circle cx="598" cy="68" r="58" fill="var(--purple)" role="img" aria-label="Mobile phone icon"/>
      <circle cx="796" cy="104" r="58" fill="var(--cream)" role="img" aria-label="Doughnut icon"/>
      <circle cx="972" cy="204" r="50" fill="var(--teal)" role="img" aria-label="House icon"/>
      <circle cx="1108" cy="400" r="58" fill="var(--yellow)" role="img" aria-label="Piggy bank icon"/>
      <circle cx="1136" cy="616" r="58" fill="var(--raspberry)" role="img" aria-label="Stethoscope icon"/>
    </g>

    <path class="host host-right" role="img" aria-label="Painted portrait of the second host in glasses and a light T-shirt"
      d="M496 828 C520 760 610 712 720 690 C735 640 730 560 730 470 C735 330 830 210 930 195 C1000 185 1060 240 1075 330 C1090 420 1075 560 1050 640 C1110 690 1180 720 1200 760 L1200 828 Z"
      fill="url(#host-right-tone)"/>

    <path class="host host-left" role="img" aria-label="Painted portrait of the first host smiling, in a blue collared shirt"
      d="M0 828 L0 690 C60 650 140 620 200 600 C180 530 170 430 190 340 C210 240 290 180 390 182 C480 184 550 240 555 340 C560 440 530 560 500 640 C560 680 620 720 664 780 L664 828 Z"
      fill="url(#host-left-tone)"/>
  </svg>

  <div class="title-band"></div>
  <div class="bottom-strip" role="img" aria-label="Faded photograph of a host wearing a shirt with a handwritten quote"></div>

  <h1 class="title">
    <span class="title-kicker">Paper</span>
    <span class="title-main">Lantern</span>
    <span class="title-main">Theory</span>
    <span class="title-format">PODCAST</span>
  </h1>
</main>
</body>
</html>
```